Coastal Heritage Dairywrights' Guild needs new business cards

We need new business cards designed and produced. We are likely to need other design work done for ads, flyers etc in future.

We would like to start with an initial business card.

The Coastal Heritage Dairywrights' Guild (CHDG) is a membership-based not-for-profit organisation that looks after the interests of Australia's small to medium artisan cheesemakers, many of whom are also small-scale farmers. The design should be simple, using our logo, but also communicate our artisan cheese and small dairy farm focus.

The first card to be designed and produced is for me, Megan Thorburn. My details are:

Megan Thorburn
Secretary
Coastal Heritage Dairywrights' Guild (CHDG)
http://www.curdandcrockery.org
T +61427583914
E megan.meganthorburn@mailfern.net

I have attached the CHDG logo in jpg form. I have a higher resolution version available if needed.

Thank you!

Megan

Business

Megan Thorburn
Coastal Heritage Dairywrights' Guild
megan.meganthorburn@mailfern.net
+61427583914

Sans Serif

• Logo (see attached file)

```html
<!DOCTYPE html>
<html lang="en">
<head>
<meta charset="utf-8">
<title>CHDG Business Card</title>
<link href="https://fonts.googleapis.com/css2?family=Source+Sans+3:wght@400;600&display=swap" rel="stylesheet">
<style>
  :root {
    --backdrop: #1f1f1f;
    --card-white: #ffffff;
    --brown: #5e3a14;
    --cheese: #fcd06b;
    --title-gold: #f5c258;
    --ink: #4a4a4a;
    --rule: #d9cbb8;
  }
  * { margin: 0; padding: 0; box-sizing: border-box; }
  html, body { width: 1200px; height: 987px; overflow: hidden; }
  body { background: var(--backdrop); position: relative; font-family: "Source Sans 3", sans-serif; }

  .card {
    position: absolute;
    left: 293px;
    width: 615px;
    height: 352px;
    border-radius: 23px;
    overflow: hidden;
  }
  .card--front { top: 130px; background: var(--card-white); }
  .card--back { top: 505px; background: var(--cheese); }

  .guild-mark { position: absolute; display: flex; align-items: center; }
  .guild-mark__dot { border-radius: 50%; flex: none; }
  .guild-mark__name {
    font-family: "Source Sans 3", sans-serif;
    font-weight: 400;
    color: var(--brown);
  }

  .card--front .guild-mark { left: 42px; top: 114px; gap: 16px; }
  .card--front .guild-mark__dot { width: 74px; height: 74px; background: var(--cheese); }
  .card--front .guild-mark__name { font-size: 20px; line-height: 22px; width: 125px; }

  .divider {
    position: absolute;
    left: 289px; top: 110px;
    width: 1px; height: 133px;
    background: var(--rule);
  }

  .contact { position: absolute; left: 313px; top: 111px; }
  .contact__name { font-size: 24px; font-weight: 600; color: var(--brown); line-height: 1.1; }
  .contact__role { font-size: 16px; font-weight: 400; color: var(--title-gold); line-height: 1.2; margin-bottom: 8px; }
  .contact__list { list-style: none; }
  .contact__item {
    display: flex; align-items: center; gap: 8px;
    font-size: 16px; color: var(--ink); height: 23.5px;
  }
  .contact__icon { width: 14px; height: 14px; flex: none; fill: var(--brown); }

  .accent-band { position: absolute; left: 0; bottom: 0; width: 615px; height: 24px; }

  .card--back .guild-mark { left: 94px; top: 100px; gap: 22px; }
  .card--back .guild-mark__dot { width: 126px; height: 126px; background: var(--brown); }
  .card--back .guild-mark__name { font-size: 28px; line-height: 32px; width: 180px; }

  .site-url {
    position: absolute; left: 0; right: 0; top: 293px;
    text-align: center;
    font-size: 16px; letter-spacing: 4.6px;
    color: var(--brown);
  }
</style>
</head>
<body>

<section class="card card--front">
  <div class="guild-mark">
    <span class="guild-mark__dot"></span>
    <p class="guild-mark__name">Coastal Heritage Dairywrights’ Guild</p>
  </div>

  <span class="divider"></span>

  <div class="contact">
    <h1 class="contact__name">Megan Thorburn</h1>
    <p class="contact__role">Secretary</p>
    <ul class="contact__list">
      <li class="contact__item">
        <svg class="contact__icon" viewBox="0 0 16 16" aria-hidden="true"><path d="M3.6 1.2l2.3 2.6-1.3 2a9 9 0 0 0 5.6 5.6l2-1.3 2.6 2.3-1.4 2.2C7.7 15.2.8 8.3 1.4 2.6z"/></svg>
        +61427583914
      </li>
      <li class="contact__item">
        <svg class="contact__icon" viewBox="0 0 16 16" aria-hidden="true"><path d="M1 3.5h14v9H1z"/><path d="M1.5 4.2l6.5 5 6.5-5" stroke="#fff" stroke-width="1.2" fill="none"/></svg>
        megan.meganthorburn@mailfern.net
      </li>
      <li class="contact__item">
        <svg class="contact__icon" viewBox="0 0 16 16" aria-hidden="true"><circle cx="8" cy="8" r="7"/><path d="M4 5c2 0 3 1 2.5 3S8 10 7 13M10 2.5c-.5 2 1 3 3 3.5" stroke="#fff" stroke-width="1.2" fill="none"/></svg>
        www.curdandcrockery.org
      </li>
    </ul>
  </div>

  <svg class="accent-band" viewBox="0 0 615 24" aria-hidden="true">
    <polygon points="0,0 398,0 392,24 0,24" fill="var(--brown)"/>
    <polygon points="404,0 615,0 615,24 398,24" fill="var(--cheese)"/>
  </svg>
</section>

<section class="card card--back">
  <div class="guild-mark">
    <span class="guild-mark__dot"></span>
    <p class="guild-mark__name">Coastal Heritage Dairywrights’ Guild</p>
  </div>
  <p class="site-url">www.curdandcrockery.org</p>
</section>

</body>
</html>
```